B2B Service Company - Word Template

We need a word template to be used as business proposals for prospective clients. Please visit our web site: www.quendapro.com.do and our Instagram Quendard for content / design ideas and to understand our branding and messaging . The color scheme must consistent with our logo, website and possibly our Instagram.

Just to be extra clear we expect the deliverable to be an actual working Microsoft word template document, with configured headers, theme, style, etc.

Target Market(s)

B2B Profesional companies

Requirements
Must have
• The color scheme must consistent with our logo, website and possibly our Instagram.

Different section headers, cover page with profesional design, back page, index section,

```html
<!DOCTYPE html>
<html lang="en">
<head>
<meta charset="utf-8">
<title>Quendapro Proposal Template – Page Overview</title>
<link href="https://fonts.googleapis.com/css2?family=Open+Sans:ital,wght@0,400;0,600;0,700;1,400&display=swap" rel="stylesheet">
<style>
:root{
  --canvas:#a7a7a7;
  --paper:#ffffff;
  --ink:#1b1b1b;
  --text:#4a4a4a;
  --teal:#3bbdd4;
  --black:#0f0f10;
  --rule:#cfcfcf;
  --row:#d7ebf7;
  --row-head:#c9c9c9;
  --link:#2b6fc4;
}
*{box-sizing:border-box;margin:0;padding:0}
html,body{width:1200px;height:1200px;overflow:hidden;background:var(--canvas)}
body{position:relative;font-family:"Open Sans",Arial,sans-serif;color:var(--text)}
.page{position:absolute;width:249px;height:352px;background:var(--paper);overflow:hidden;box-shadow:0 0 2px rgba(0,0,0,.25)}
.client{position:absolute;top:9px;right:17px;font-size:3.2px;line-height:4px;color:var(--ink);letter-spacing:.1px;white-space:nowrap}
.title{position:absolute;top:22px;left:21px;right:21px;text-align:center;font-size:8.6px;color:var(--ink);letter-spacing:.2px;padding-bottom:3px;border-bottom:.6px solid var(--rule)}
.title::after{content:"";position:absolute;left:0;right:0;bottom:-3px;border-bottom:.6px solid var(--rule)}
.body{position:absolute;top:44px;left:21px;right:21px}
.p{font-size:3.3px;line-height:4.7px;margin-bottom:4px;color:var(--text)}
.p.center{text-align:center}
.h2{font-size:6.4px;color:var(--teal);margin:4px 0 1.5px}
.lead{font-size:6.4px;line-height:8px;color:var(--teal);margin-bottom:5px}
.ital{font-style:italic}
.link{color:var(--link);text-decoration:underline}
.footer{position:absolute;left:0;bottom:11px;width:72px;height:7px}
.footer svg{display:block}
.brand{font-weight:700;color:#fff;letter-spacing:.5px}
.footer .brand{position:absolute;left:20px;top:.6px;font-size:4.6px;line-height:5.5px}
.pnum{position:absolute;right:17px;bottom:12px;font-size:3.4px;color:var(--ink)}
.photo{background:linear-gradient(135deg,#3a4f6d 0%,#8aa6c4 45%,#cfdbe7 70%,#2c3c55 100%)}
table{border-collapse:separate;border-spacing:1px;width:100%;font-size:3.1px;color:var(--ink)}
td,th{padding:.6px 2px;height:5.6px}
th{background:var(--row-head);font-weight:400;color:#fff;text-align:center}
td{background:var(--row)}
td.c{text-align:center}
tr.sec td{font-weight:700;color:var(--ink)}
tr.tot td{background:#e3e3e3;font-weight:700}
tr.grand td{background:var(--teal);color:#fff;font-weight:700}
.tl th{background:var(--teal)}
.tl td{background:#e6e6e6}
/* cover */
.cover-logo{position:absolute;top:109px;right:21px;text-align:right}
.cover-logo .name{font-size:17px;font-weight:700;color:var(--ink);letter-spacing:1px;line-height:18px}
.cover-logo .tag{font-size:6.2px;color:var(--ink);line-height:7px}
.cover-band{position:absolute;left:16px;top:149px;width:233px;height:84px}
.cover-head{position:absolute;right:21px;top:168px;text-align:right;color:#fff;font-size:10px;line-height:13px;letter-spacing:.2px}
.cover-sub{position:absolute;right:21px;top:208px;color:var(--teal);font-size:6.6px;font-weight:600}
/* toc */
.toc-h{font-size:5.8px;color:var(--ink);margin:22px 0 9px}
.toc-row{display:flex;align-items:baseline;font-size:3.1px;line-height:8.2px;color:var(--ink)}
.toc-row .lab{white-space:nowrap}
.toc-row .dots{flex:1;border-bottom:.5px dotted #555;margin:0 3px;transform:translateY(-1px)}
.toc-row.b .lab{font-weight:700}
.toc-row.i1{padding-left:4px}
.toc-row.i2{padding-left:8px}
/* vision banner */
.banner{display:flex;align-items:center;background:var(--black);height:22px;margin-bottom:9px}
.banner .ico{width:25px;height:22px;background:var(--teal);display:flex;align-items:center;justify-content:center;flex:none}
.banner .txt{color:#fff;font-size:3.5px;line-height:4.4px;padding:0 6px 0 5px}
/* legend */
.legend{display:grid;grid-template-columns:repeat(4,1fr);gap:4px 2px;font-size:2.7px;color:var(--ink);margin:6px 6px 0}
.legend span{display:flex;align-items:center;gap:2px;white-space:nowrap}
.legend i{display:inline-block;width:5px;height:5px;flex:none}
.stripes div{height:9px;background:var(--row);margin-bottom:4px}
/* back */
.back-band{position:absolute;left:0;bottom:23px;width:249px;height:11px}
.back-logo{position:absolute;left:73px;bottom:22px;text-align:center;width:48px}
.back-logo .name{font-size:7px;font-weight:700;color:var(--ink);letter-spacing:.3px;line-height:8px}
.back-logo .tag{font-size:2.6px;line-height:3px;color:var(--ink)}
.back-info{position:absolute;bottom:22px;font-size:2.6px;line-height:3.5px;color:var(--ink);white-space:nowrap}
</style>
</head>
<body>

<!-- Cover -->
<section class="page" style="left:62px;top:47px">
  <div class="cover-logo">
    <div class="name">QUENDAPRO</div>
    <div class="tag">soluciones para tu empresa</div>
  </div>
  <svg class="cover-band" viewBox="0 0 233 84" width="233" height="84">
    <polygon points="0,84 49,0 55,0 6,84" fill="var(--teal)"/>
    <polygon points="11,84 60,0 233,0 233,84" fill="var(--black)"/>
  </svg>
  <div class="cover-head">LOREM IPSUM IS SIMPLY<br>DUMMY HAS BEEN</div>
  <div class="cover-sub">LOREM IPSUM IS SIMPLY ETIAM</div>
</section>

<!-- Copyright page -->
<section class="page" style="left:340px;top:47px">
  <div style="position:absolute;left:69px;top:292px;width:.8px;height:21px;background:var(--teal)"></div>
  <div style="position:absolute;left:77px;top:292px;font-size:2.6px;line-height:3.6px;color:var(--ink)">
    Copyright © 2020 Quenda Services Group.<br>All Rights Reserved.<br>
    No part of the contents of this document may be reproduced or distributed in any form or by<br>any means without the prior written permission of Quenda Services Group.
  </div>
</section>

<!-- Table of contents -->
<section class="page" style="left:617px;top:47px">
  <div class="client">THE CLIENT NAME</div>
  <div class="title">TABLE OF CONTENTS</div>
  <div class="body" style="top:38px">
    <div class="toc-h">Contents</div>
    <div class="toc-row b"><span class="lab">1. Table of Contents</span><span class="dots"></span><span>01</span></div>
    <div class="toc-row i1"><span class="lab">1.1. Executive Summary</span><span class="dots"></span><span>02</span></div>
    <div class="toc-row i2"><span class="lab">1.1.1. Our Understanding of Your Needs</span><span class="dots"></span><span>02</span></div>
    <div class="toc-row b"><span class="lab">2. Our Recommendations</span><span class="dots"></span><span>03</span></div>
    <div class="toc-row i1"><span class="lab">2.1. Our Approach</span><span class="dots"></span><span>05</span></div>
    <div class="toc-row i2"><span class="lab">2.1.1. Budget and Timeframe</span><span class="dots"></span><span>07</span></div>
    <div class="toc-row"><span class="lab">3. Appendix A: About Brookfield Lane</span><span class="dots"></span><span>10</span></div>
    <div class="toc-row i1"><span class="lab">3.1. Appendix B: Selected Client List</span><span class="dots"></span><span>10</span></div>
    <div class="toc-row i2"><span class="lab">3.1.1. Appendix C: Our Capabilities</span><span class="dots"></span><span>11</span></div>
    <div class="toc-row"><span class="lab">Appendix D: Our Process</span><span class="dots"></span><span>12</span></div>
  </div>
  <div class="footer"><svg width="72" height="7" viewBox="0 0 72 7"><polygon points="0,0 60,0 66,7 0,7" fill="var(--black)"/><polygon points="60,0 64,0 70,7 66,7" fill="var(--teal)"/></svg><span class="brand">QUENDAPRO</span></div>
</section>

<!-- Vision -->
<section class="page" style="left:892px;top:47px">
  <div class="client">THE CLIENT NAME</div>
  <div class="title">VISION</div>
  <div class="body">
    <div class="banner">
      <div class="ico"><svg width="16" height="16" viewBox="0 0 16 16"><circle cx="8" cy="8" r="6.5" fill="none" stroke="#fff" stroke-width="1.2"/><circle cx="8" cy="8" r="3.8" fill="none" stroke="#fff" stroke-width="1.2"/><circle cx="8" cy="8" r="1.3" fill="#fff"/><line x1="8" y1="8" x2="14" y2="2" stroke="#fff" stroke-width="1"/></svg></div>
      <div class="txt">Tallyo's mission is to help and support the self-employed and small business owners with their administrative tasks so they can focus on what matters – their business.</div>
    </div>
    <p class="p">Administrative tasks are cumbersome, time-consuming and often prevent small owners from focusing their time and energy on their business and their customers. They can also be extremely stressful and nerve-wracking for those attempting these tasks for the first time.</p>
    <p class="p center">At Tallyo, we envisage accounting for the self-employed and small business owners as being fully automated and decentralized</p>
    <p class="p">Accounting can and should be done automatically. By connecting to all sources of accounting data such as bank accounts, payment systems, e-commerce websites, and invoicing systems, Tallyo AI automatically completes these tasks, which would take hours to do manually. Bookings are created automatically and fully completed. Financial statements are available within a couple of clicks, and after analysing your data, Tallyo AI will offer you tips to improve your financial stability.</p>
    <p class="p">What may seem like a pipedream to the millions of self-employed who struggle with their admin, is already a reality. Now is the time to join Tallyo on its mission to transform the world of bookkeeping through the power of AI.</p>
    <div class="h2">The Tallyo model</div>
    <p class="p">Tallyo is based on an innovative license model that uses Tokens-as-a-License (TaaL). The token represents lifelong software license for Tallyo solutions. The Pre-ICO token sales will enable Tallyo to complete its development of Tallyo AI to deliver fully automatic bookkeeping.</p>
    <p class="p">The Pre-ICO token sale will also pave the way for a future Tallyo ICO. Tallyo will launch accounting on the blockchain and ensure your accounting data is comprehensive and private, but available everywhere within your preferred apps. It will empower you to manage your data as you see fit in a fully decentralized way. Furthermore, a new range of business apps will connect to Tallyo to provide you</p>
    <p class="p">with leading edge business data access to ensure you have the best available data at your fingertips.</p>
    <p class="p">Tallyo supports strong data ownership laws that truly protect individuals and ensure they have complete ownership of their data. Through decentralisation Tallyo helps to ensure you always have full ownership of your data to decide how it should be used.</p>
    <p class="p">To find out more about the Tallyo AI project, and the Tallyo TaaL or if you are interested in purchasing Tallyo TaaL, please register with your email at <span class="link">https://www.tallyo.example/ico</span> so we can notify you about our upcoming purchase periods.</p>
  </div>
  <div class="footer"><svg width="72" height="7" viewBox="0 0 72 7"><polygon points="0,0 60,0 66,7 0,7" fill="var(--black)"/><polygon points="60,0 64,0 70,7 66,7" fill="var(--teal)"/></svg><span class="brand">QUENDAPRO</span></div>
  <div class="pnum">2</div>
</section>

<!-- Budget and timeframe -->
<section class="page" style="left:62px;top:430px">
  <div class="client">THE CLIENT NAME</div>
  <div class="title">BUDGET AND TIMEFRAME</div>
  <div class="body">
    <div class="h2" style="margin-top:0">Implementation Estimate</div>
    <p class="p">The bulk of the implementation costs will be defined by discovery. Based on similar CRM implementation projects, we feel expect that the CRM side will be something between 200 and 300 hours, give or take. The wide swing in hours in phase one is related currently to the undefined nature of both the integration needs and our role in the integration project. Our focus in discovery (as mentioned above) will be to nail down and finalize those requirements and our role as it relates to what is needed to integrate the sites with the CRM.</p>
    <table style="margin-top:6px">
      <tr><th style="width:55%">Task</th><th>Hours</th><th>Cost</th></tr>
      <tr><td>Discovery</td><td class="c">40</td><td class="c">$8,000</td></tr>
      <tr class="sec"><td colspan="3">Phase 1</td></tr>
      <tr><td>Discovery</td><td class="c">20-40</td><td class="c">$8,000</td></tr>
      <tr><td>Discovery</td><td class="c">20-40</td><td class="c">$8,000</td></tr>
      <tr><td>Discovery</td><td class="c">20-40</td><td class="c">$8,000</td></tr>
      <tr class="tot"><td>Total Phase 1</td><td class="c">80-240</td><td class="c">$16,800-40,000</td></tr>
      <tr class="sec"><td colspan="3">Phase 2</td></tr>
      <tr><td>Discovery</td><td class="c">20-40</td><td class="c">$8,000</td></tr>
      <tr class="tot"><td>Total Phase 2</td><td class="c">80-240</td><td class="c">$16,800-40,000</td></tr>
      <tr class="grand"><td>Total Estimated Implementation Cost</td><td class="c">220-480</td><td class="c">$44,000-96,000</td></tr>
    </table>
    <div class="h2" style="margin-top:14px">Project Timeline</div>
    <p class="p">Based on the information we have out our disposal, the March 21st launch date doesn't seem a realistic goal to get both the work done needed to provide the foundation for the future CRM instance and the integration given the state of apparent flux of the requirements. That said, we feel it prudent to proceed with discovery before committing to or pushing that date. We are currently estimating that the first phase will take somewhere between 7 and 12 weeks (including discovery) to complete.</p>
    <table class="tl" style="margin-top:6px">
      <tr><th style="width:62%">Task</th><th>Weeks to Complete</th></tr>
      <tr><td>Discovery</td><td class="c">1-2</td></tr>
      <tr><td>Phase 1</td><td class="c">6-10</td></tr>
      <tr><td>Phase 2</td><td class="c">8-12</td></tr>
      <tr><td>Total Number of Weeks</td><td class="c"></td></tr>
    </table>
  </div>
  <div class="footer"><svg width="72" height="7" viewBox="0 0 72 7"><polygon points="0,0 60,0 66,7 0,7" fill="var(--black)"/><polygon points="60,0 64,0 70,7 66,7" fill="var(--teal)"/></svg><span class="brand">QUENDAPRO</span></div>
  <div class="pnum">3</div>
</section>

<!-- Our understanding -->
<section class="page" style="left:340px;top:430px">
  <div class="client">THE CLIENT NAME</div>
  <div class="title">OUR UNDERSTANDING OF YOUR NEEDS</div>
  <div class="body">
    <div class="lead">Tallyo's mission is to help and support the<br>self-employed and small business owners with</div>
    <svg width="207" height="84" viewBox="-103.5 -44 207 84" role="img" aria-label="Pie chart of share by country">
      <g transform="translate(2,0)">
        <path d="M0,0 L0,-40 A40,40 0 0 1 37.6,13.6 Z" fill="#6cb6e0"/>
        <path d="M0,0 L37.6,13.6 A40,40 0 0 1 3,39.9 Z" fill="#5b8fd6"/>
        <path d="M0,0 L3,39.9 A40,40 0 0 1 -25.5,30.8 Z" fill="#4f70c8"/>
        <path d="M0,0 L-25.5,30.8 A40,40 0 0 1 -38.8,9.7 Z" fill="#6a62c2"/>
        <path d="M0,0 L-38.8,9.7 A40,40 0 0 1 -38.3,-11.4 Z" fill="#8660c4"/>
        <path d="M0,0 L-38.3,-11.4 A40,40 0 0 1 -28.5,-28.1 Z" fill="#a264c6"/>
        <path d="M0,0 L-28.5,-28.1 A40,40 0 0 1 -16.1,-36.6 Z" fill="#c06ac8"/>
        <path d="M0,0 L-16.1,-36.6 A40,40 0 0 1 -7.5,-39.3 Z" fill="#d66fb8"/>
        <path d="M0,0 L-7.5,-39.3 A40,40 0 0 1 0,-40 Z" fill="#e0739a"/>
      </g>
      <g font-size="2.6" fill="#333" font-family="Open Sans, sans-serif">
        <text x="46" y="-15">Lithuania  30.5%</text>
        <text x="44" y="24">Czech Republic  18.3%</text>
        <g text-anchor="end">
          <text x="-44" y="-32">The Netherlands  3.0%</text>
          <text x="-44" y="-26">Belgium  3.6%</text>
          <text x="-44" y="-20">UK  6.0%</text>
          <text x="-44" y="-14">Austria  7.8%</text>
          <text x="-44" y="-8">Australia  8.5%</text>
          <text x="-44" y="12">Germany  10.1%</text>
          <text x="-34" y="32">Ireland  12.2%</text>
        </g>
      </g>
    </svg>
    <div class="legend">
      <span><i style="background:#6cb6e0"></i>Lithuania 30.5%</span>
      <span><i style="background:#5b8fd6"></i>Czech Republic 18.3%</span>
      <span><i style="background:#4f70c8"></i>Ireland 12.2%</span>
      <span><i style="background:#6a62c2"></i>Germany 10.1%</span>
      <span><i style="background:#8660c4"></i>Australia 8.5%</span>
      <span><i style="background:#a264c6"></i>Austria 7.8%</span>
      <span><i style="background:#c06ac8"></i>UK 6.0%</span>
      <span><i style="background:#d66fb8"></i>Belgium 3.6%</span>
      <span><i style="background:#e0739a"></i>The Netherlands 3.0%</span>
    </div>
    <div class="h2" style="margin-top:34px">Lorem Ipsum</div>
    <p class="p">The bulk of the implementation costs will be defined by discovery. Based on similar CRM implementation projects, we feel expect that the CRM side will be something between 200 and 300 hours, give or take. The wide swing in hours in phase one is related currently to the undefined nature of both the integration needs and our role in the integration project. Our focus in discovery (as mentioned above) will be to nail down and finalize those requirements and our role as it relates to what is needed to integrate the sites with the CRM.</p>
    <p class="p">The bulk of the implementation costs will be defined by discovery. Based on similar CRM implementation projects, we feel expect that the CRM side will be something between 200 and 300 hours, give or take. The wide swing in hours in phase one is related currently to the undefined nature of both the integration needs and our role in the integration project. Our focus in discovery (as mentioned above) will be to nail down and finalize those requirements and our role as it relates to what is needed to integrate the sites with the CRM.</p>
  </div>
  <div class="footer"><svg width="72" height="7" viewBox="0 0 72 7"><polygon points="0,0 60,0 66,7 0,7" fill="var(--black)"/><polygon points="60,0 64,0 70,7 66,7" fill="var(--teal)"/></svg><span class="brand">QUENDAPRO</span></div>
  <div class="pnum">4</div>
</section>

<!-- Headline page with wide photo -->
<section class="page" style="left:617px;top:430px">
  <div class="client">THE CLIENT NAME</div>
  <div class="title">HEADLINE HERE</div>
  <div class="body">
    <div class="photo" role="img" aria-label="Photo of a businessman sketching cloud and network icons on glass" style="height:89px;margin-bottom:7px"></div>
    <div class="lead">Tallyo's mission is to help and support the<br>self-employed and small business owners with</div>
    <p class="p">Administrative tasks are cumbersome, time-consuming and often prevent small owners from focusing their time and energy on their business and their customers. They can also be extremely stressful and nerve-wracking for those attempting these tasks for the first time.</p>
    <p class="p">At Tallyo, we envisage accounting for the self-employed and small business owners as being <span class="link">automated and decentralized</span></p>
    <div class="stripes" style="margin:4px 6px 0;border-top:.6px solid #b9cfe0;padding-top:7px">
      <div></div><div></div><div></div><div></div>
    </div>
    <div class="h2" style="margin-top:7px">The Tallyo model</div>
    <p class="p">Tallyo is based on an innovative license model that uses Tokens-as-a-License (TaaL). The token represents lifelong software license for Tallyo solutions. The Pre-ICO token sales will enable Tallyo to complete its development of Tallyo AI to deliver fully automatic bookkeeping.</p>
    <p class="p">with leading edge business data access to ensure you have the best available data at your fingertips.</p>
  </div>
  <div class="footer"><svg width="72" height="7" viewBox="0 0 72 7"><polygon points="0,0 60,0 66,7 0,7" fill="var(--black)"/><polygon points="60,0 64,0 70,7 66,7" fill="var(--teal)"/></svg><span class="brand">QUENDAPRO</span></div>
  <div class="pnum">5</div>
</section>

<!-- Executive summary -->
<section class="page" style="left:892px;top:430px">
  <div class="client">THE CLIENT NAME</div>
  <div class="title">EXECUTIVE SUMMARY</div>
  <div class="body" style="top:47px;left:25px;right:25px">
    <div class="h2" style="margin-top:0">Solution</div>
    <p class="p ital" style="margin-bottom:1px">AI automated accounting</p>
    <p class="p">Tallyo builds automation in stages on top of its current system to reach full automation thanks to the Tallyo AI. Tallyo AI automates every manual task performed by the user. It starts by connecting to all sources of accounting data such as bank accounts, e-commerce, webshop or document management systems (shared cloud drives). Based on these data, Tallyo AI creates bookings and generates financial reports. Finally, Tallyo AI features chat-like interface that allows users to communicate seamlessly with it, viewing it as a trusted advisor over time for all their accounting queries.</p>
    <p class="p ital" style="margin-bottom:1px">Blockchain software license or Token-as-a-License (TaaL)</p>
    <p class="p">It is possible to create tokens on blockchain that represent software licenses, also known as Token-as-a-Licence (TaaL). Tallyo creates TaaL by using the Corvel official wallet which interacts with the Corvel blockchain. Upon purchase of TaaL, the token holder is free to transfer or sell TaaL using secondary market that is built directly over the blockchain, in our case, the Corvel marketplace. Tallyo checks the validity of a token against the blockchain ensuring that token holders have access to the software. TaaL make distribution and securisation of software licenses easier for software developers. It also makes the management and resale of software license easier for software owners. All in all, TaaL has a higher value as a normal software license.</p>
    <div class="h2">Pre-ICO Token sale</div>
    <p class="p">To realize this innovative vision, Tallyo is launching a pre-ICO in form of a token sale on Corvel blockchain. 20,000,000 tokens are available to purchase for the price of CHF 0.10 each during a 30-day period to be announced. Tokens represent Tallyo lifelong software licenses and by purchasing enough tokens, holders gain access to Tallyo software. 15,000 tokens give access to Tallyo invoicing or accounting. 20,000 tokens give access to both Tallyo accounting and invoicing. Future customers will still have the opportunity to buy directly yearly or monthly subscriptions to have access to Tallyo.</p>
    <div class="h2">Future plans</div>
    <p class="p">A future ICO is planned between 18 and 24 months after the pre-ICO token sale. This offering will support the development of Tallyo into a fully decentralized, privacy-focused ecosystem of applications. The new model will reward each participant so that a new world with zero administrative tasks becomes reality.</p>
  </div>
  <div class="footer"><svg width="72" height="7" viewBox="0 0 72 7"><polygon points="0,0 60,0 66,7 0,7" fill="var(--black)"/><polygon points="60,0 64,0 70,7 66,7" fill="var(--teal)"/></svg><span class="brand">QUENDAPRO</span></div>
  <div class="pnum">1</div>
</section>

<!-- Headline page with side photos -->
<section class="page" style="left:62px;top:814px">
  <div class="client">THE CLIENT NAME</div>
  <div class="title">HEADLINE HERE</div>
  <div class="photo" role="img" aria-label="Photo of a businessman drawing cloud and arrow icons" style="position:absolute;left:21px;top:45px;width:87px;height:110px"></div>
  <div class="photo" role="img" aria-label="Close-up photo of a hand sketching a cloud network diagram" style="position:absolute;left:21px;top:199px;width:87px;height:116px"></div>
  <div style="position:absolute;left:124px;top:45px;right:24px">
    <p style="font-size:5px;line-height:5.4px;font-weight:700;color:var(--ink);margin-bottom:6px">Tallyo's mission is to help and support the self-employed and small business owners with their administrative tasks so they can focus on what matters -- their business.</p>
    <p class="p">Administrative tasks are cumbersome, time-consuming and often prevent small owners from focusing their time and energy on their business and their customers. They can also be extremely stressful and nerve-wracking for those attempting these tasks for the first time.</p>
    <p class="p">At Tallyo, we envisage accounting for the self-employed and small business owners as being <span class="link">automated and decentralized</span></p>
    <p class="p">Accounting can and should be done automatically. By connecting to all sources of accounting data such as bank accounts, payment systems, e-commerce websites, and invoicing systems, Tallyo AI automatically completes these tasks, which would take hours to do manually. Bookings are created automatically and fully completed. Financial statements are available within a couple of clicks, and after analysing your data, Tallyo AI will offer you tips to improve your financial stability.</p>
    <p class="p">What may seem like a pipedream to the millions of self-employed who struggle with</p>
    <div class="h2" style="margin-top:5px">The Tallyo model</div>
    <p class="p">Tallyo is based on an innovative license model that uses Token-as-a-License (TaaL). The token represents lifelong software license for Tallyo solutions. The Pre-ICO token sales will enable Tallyo to complete its development of Tallyo AI to deliver fully automatic</p>
  </div>
  <div class="footer"><svg width="72" height="7" viewBox="0 0 72 7"><polygon points="0,0 60,0 66,7 0,7" fill="var(--black)"/><polygon points="60,0 64,0 70,7 66,7" fill="var(--teal)"/></svg><span class="brand">QUENDAPRO</span></div>
  <div class="pnum">6</div>
</section>

<!-- Back page -->
<section class="page" style="left:340px;top:814px">
  <svg class="back-band" width="249" height="11" viewBox="0 0 249 11">
    <polygon points="0,0 58,0 67,11 0,11" fill="var(--black)"/>
    <polygon points="58,0 62,0 71,11 67,11" fill="var(--teal)"/>
  </svg>
  <div class="back-logo">
    <div class="name">QUENDAPRO</div>
    <div class="tag">soluciones para tu empresa</div>
  </div>
  <div class="back-info" style="left:128px;padding-left:3px;border-left:.5px solid #999">
    P: (809) 555-0142 (ext 101)<br>E: hello@quendapro.com.do<br>W: www.quendapro.com.do
  </div>
  <div class="back-info" style="left:172px;padding-left:3px;border-left:.5px solid #999">
    210, 48 Harbour View Road<br>Lakemont, North Province 10114
  </div>
</section>

</body>
</html>
```